Rollup banners

Need a design similar to the uploaded PDF file. Task is to create 3 designs to promote our school's qualifications.
1st Design should promote:
-KPL DIPLOMA IN FASHION TECHNOLOGY (APPAREL DESIGN AND PRODUCT DEVELOPMENT)
-KPL DIPLOMA IN FASHION TECHNOLOGY (MERCHANDISING AND MARKETING)
-KPL ADVANCED CERTIFICATE IN FASHION TECHNOLOGY (APPAREL DESIGN AND PRODUCT DEVELOPMENT)
-KPL ADVANCED CERTIFICATE IN FASHION TECHNOLOGY (MERCHANDISING AND MARKETING)
2nd Design:
-KPL DIPLOMA IN FASHION TECHNOLOGY (FOOTWEAR DESIGN AND PRODUCT DEVELOPMENT)
3rd Design:
Professional short Courses:
-Fashion Styling
-Sewing
-Fashion Entrepreneurship
-Leather Care
-Fabric Care
Background on our business(For your own knowledge): Our company is called Harlow and Vine Training Center (HaV.tc). We help train the fashion industry as well as over diploma programmes for people who are interested in joining the fashion industry.
Audience: General Public, Fashionistas, Fashion Students, Aspiring Footwear Enthusiasts and people interested to enter the fashion industry
Must Have:
-Take color scheme from uploaded PDF file
-Hex code for corporate color is #DA291C (Red)
- Corporate Colors to be Included: Grey, White, Black
Banner size: 850 X 2000mm
I've also attached our logos for you to use.
Please note that in the footer: please put the NB PLX Centre, Vero Mark Singapore.
You may choose to use either version of the logos- HaV.tc in Red ciricle or Typeface HaV.tc

```html
<!DOCTYPE html>
<html lang="en">
<head>
<meta charset="utf-8">
<title>Harlow and Vine Training Center Rollup Banners</title>
<link href="https://fonts.googleapis.com/css2?family=Dosis:wght@400;500;600&family=Open+Sans:wght@400;600&display=swap" rel="stylesheet">
<style>
  :root{
    --red:#DA291C;
    --black:#1b1b1b;
    --grey-light:#e4e4e4;
    --grey-mid:#d2d2d2;
    --white:#f7f7f7;
    --stage:#3b3b3b;
    --text:#2a2a2a;
  }
  *{box-sizing:border-box;margin:0;padding:0}
  html,body{width:1200px;height:900px;overflow:hidden}
  body{background:var(--stage);display:flex;align-items:center;justify-content:center;gap:24px}
  .banner{position:relative;width:270px;height:620px;background:var(--white);overflow:hidden;font-family:"Open Sans",sans-serif;color:var(--text)}
  .banner-shapes{position:absolute;inset:0;width:270px;height:620px}
  .photo{position:absolute;inset:0;clip-path:polygon(0 72px,270px 106px,270px 330px,0 282px)}
  .photo--portrait{background:linear-gradient(135deg,#dfe6d6 0%,#c9d3c0 45%,#b8424a 75%,#e9e3d6 100%)}
  .photo--pattern{background:linear-gradient(160deg,#eef0f2 0%,#e6c77a 50%,#f3f1ec 100%)}
  .photo--studio{background:linear-gradient(120deg,#8f8f8f 0%,#e2e2e2 45%,#bdbdbd 70%,#6d5b4d 100%)}
  .photo--runway{background:linear-gradient(150deg,#4a6a8a 0%,#2f4f6f 55%,#8c3a2c 80%,#4b6a86 100%)}
  .brand{position:absolute;top:20px;right:18px;text-align:right;font-family:"Dosis",sans-serif;font-weight:500;font-size:15px;line-height:16px;color:var(--black)}
  .headline{position:absolute;left:0;right:0;text-align:center;font-family:"Dosis",sans-serif;font-weight:500;color:var(--red);font-size:20px;line-height:23px;letter-spacing:.3px}
  .rule{display:block;width:180px;height:3px;background:var(--red);margin:6px auto 0}
  .details{position:absolute;left:16px;right:12px;font-size:7.4px;line-height:10px}
  .details h3{font-size:8px;font-weight:600;margin-top:5px;text-transform:uppercase}
  .details h3:first-child{margin-top:0}
  .intro{font-family:"Dosis",sans-serif;font-size:11px;font-weight:500;margin-bottom:6px}
  .course-list{list-style:none;font-family:"Dosis",sans-serif;font-size:12px;line-height:15px;padding-left:8px}
  .contacts{position:absolute;left:8px;top:566px;color:#fff;font-size:6px;line-height:9px;list-style:none}
  .contacts li{display:flex;align-items:center;gap:3px}
  .contacts svg{width:6px;height:6px}
  .partners{position:absolute;right:12px;top:576px;display:flex;gap:10px;align-items:center;font-family:"Dosis",sans-serif;font-weight:600;font-size:9px;color:var(--red)}
  .partner{display:flex;align-items:center;gap:3px}
  .partner-square{width:9px;height:9px;background:var(--red)}
  .partner-circle{width:10px;height:10px;border-radius:50%;background:var(--red)}
</style>
</head>
<body>

<!-- Banner: short courses -->
<section class="banner">
  <svg class="banner-shapes" viewBox="0 0 270 620" aria-hidden="true">
    <rect width="270" height="620" fill="var(--white)"/>
    <polygon points="0,0 270,0 270,100 0,66" fill="var(--grey-light)"/>
    <polygon points="0,62 270,96 270,106 0,72" fill="var(--black)"/>
    <polygon points="0,282 270,330 270,340 0,292" fill="var(--black)"/>
    <polygon points="0,292 160,320 0,360" fill="var(--grey-mid)"/>
    <polygon points="0,540 125,598 0,598" fill="var(--red)"/>
    <polygon points="150,598 270,560 270,620 150,620" fill="var(--grey-light)"/>
  </svg>
  <div class="photo photo--portrait" role="img" aria-label="Editorial fashion portrait of a model with a feathered headpiece and floral dress"></div>
  <div class="brand">Harlow and Vine<br>Training Center</div>
  <h2 class="headline" style="top:348px">STEP INTO THE<br>WORLD OF FASHION<span class="rule"></span></h2>
  <div class="details" style="top:410px">
    <p class="intro">PROFESSIONAL KPL SHORT COURSES IN</p>
    <ul class="course-list">
      <li>Fashion Styling</li>
      <li>Sewing &amp; Alteration</li>
      <li>Leather Care</li>
      <li>Fabric Care</li>
      <li>More courses available</li>
    </ul>
  </div>
  <ul class="contacts">
    <li><svg viewBox="0 0 10 10"><path d="M2 1l2 2-1 1.5a6 6 0 0 0 2.5 2.5L7 6l2 2-1.5 1.5C4 9 1 6 .5 2.5z" fill="#fff"/></svg>64208830</li>
    <li><svg viewBox="0 0 10 10"><rect x="0.5" y="2" width="9" height="6" fill="none" stroke="#fff"/><path d="M.5 2l4.5 3.5L9.5 2" fill="none" stroke="#fff"/></svg>enquiry@havtc.org</li>
    <li><svg viewBox="0 0 10 10"><circle cx="5" cy="5" r="4.2" fill="none" stroke="#fff"/><path d="M1 5h8M5 1v8" stroke="#fff"/></svg>www.havtc.edu.sg</li>
  </ul>
  <div class="partners">
    <span class="partner"><span class="partner-square"></span>NB PLX Centre</span>
    <span class="partner"><span class="partner-circle"></span>Vero Mark</span>
  </div>
</section>

<!-- Banner: apparel -->
<section class="banner">
  <svg class="banner-shapes" viewBox="0 0 270 620" aria-hidden="true">
    <rect width="270" height="620" fill="var(--white)"/>
    <polygon points="0,0 270,0 270,100 0,66" fill="var(--grey-light)"/>
    <polygon points="0,62 270,96 270,106 0,72" fill="var(--black)"/>
    <polygon points="0,282 270,330 270,340 0,292" fill="var(--black)"/>
    <polygon points="0,292 160,320 0,360" fill="var(--grey-mid)"/>
    <polygon points="0,540 125,598 0,598" fill="var(--red)"/>
    <polygon points="150,598 270,560 270,620 150,620" fill="var(--grey-light)"/>
  </svg>
  <div class="photo photo--pattern" role="img" aria-label="Hands measuring fabric over garment pattern sheets"></div>
  <div class="brand">Harlow and Vine<br>Training Center</div>
  <h2 class="headline" style="top:332px">APPAREL<br>DESIGN AND PRODUCT<br>DEVELOPMENT<span class="rule"></span></h2>
  <div class="details" style="top:418px">
    <h3>KPL Diploma in Fashion Technology</h3>
    <p>+ 3 months Full-Time or 1 year Part-Time Programme<br>+ 13 industry-focused KPL modules</p>
    <h3>KPL Advanced Certificate in Fashion Technology</h3>
    <p>+ Part-Time Programme up to 7 months<br>+ 6 industry-focused KPL modules</p>
    <h3>Funding &amp; Career Opportunities</h3>
    <p>Speak to us today about your eligibility in funding and potential career opportunities.</p>
  </div>
  <ul class="contacts">
    <li><svg viewBox="0 0 10 10"><path d="M2 1l2 2-1 1.5a6 6 0 0 0 2.5 2.5L7 6l2 2-1.5 1.5C4 9 1 6 .5 2.5z" fill="#fff"/></svg>64208830</li>
    <li><svg viewBox="0 0 10 10"><rect x="0.5" y="2" width="9" height="6" fill="none" stroke="#fff"/><path d="M.5 2l4.5 3.5L9.5 2" fill="none" stroke="#fff"/></svg>enquiry@havtc.org</li>
    <li><svg viewBox="0 0 10 10"><circle cx="5" cy="5" r="4.2" fill="none" stroke="#fff"/><path d="M1 5h8M5 1v8" stroke="#fff"/></svg>www.havtc.edu.sg</li>
  </ul>
  <div class="partners">
    <span class="partner"><span class="partner-square"></span>NB PLX Centre</span>
    <span class="partner"><span class="partner-circle"></span>Vero Mark</span>
  </div>
</section>

<!-- Banner: merchandising -->
<section class="banner">
  <svg class="banner-shapes" viewBox="0 0 270 620" aria-hidden="true">
    <rect width="270" height="620" fill="var(--white)"/>
    <polygon points="0,0 270,0 270,100 0,66" fill="var(--grey-light)"/>
    <polygon points="0,62 270,96 270,106 0,72" fill="var(--black)"/>
    <polygon points="0,282 270,330 270,340 0,292" fill="var(--black)"/>
    <polygon points="0,292 160,320 0,360" fill="var(--grey-mid)"/>
    <polygon points="0,540 125,598 0,598" fill="var(--red)"/>
    <polygon points="150,598 270,560 270,620 150,620" fill="var(--grey-light)"/>
  </svg>
  <div class="photo photo--studio" role="img" aria-label="Fashion merchant working on a laptop beside a clothing rail"></div>
  <div class="brand">Harlow and Vine<br>Training Center</div>
  <h2 class="headline" style="top:350px">MERCHANDISING<br>AND MARKETING<span class="rule"></span></h2>
  <div class="details" style="top:418px">
    <h3>KPL Diploma in Fashion Technology</h3>
    <p>+ 3 months Full-Time or 1 year Part-Time Programme<br>+ 13 industry-focused KPL modules</p>
    <h3>KPL Advanced Certificate in Fashion Technology</h3>
    <p>+ Part-Time Programme up to 5 months<br>+ 6 industry-focused KPL modules</p>
    <h3>Funding &amp; Career Opportunities</h3>
    <p>Speak to us today about your eligibility in funding and potential career opportunities.</p>
  </div>
  <ul class="contacts">
    <li><svg viewBox="0 0 10 10"><path d="M2 1l2 2-1 1.5a6 6 0 0 0 2.5 2.5L7 6l2 2-1.5 1.5C4 9 1 6 .5 2.5z" fill="#fff"/></svg>64208830</li>
    <li><svg viewBox="0 0 10 10"><rect x="0.5" y="2" width="9" height="6" fill="none" stroke="#fff"/><path d="M.5 2l4.5 3.5L9.5 2" fill="none" stroke="#fff"/></svg>enquiry@havtc.org</li>
    <li><svg viewBox="0 0 10 10"><circle cx="5" cy="5" r="4.2" fill="none" stroke="#fff"/><path d="M1 5h8M5 1v8" stroke="#fff"/></svg>www.havtc.edu.sg</li>
  </ul>
  <div class="partners">
    <span class="partner"><span class="partner-square"></span>NB PLX Centre</span>
    <span class="partner"><span class="partner-circle"></span>Vero Mark</span>
  </div>
</section>

<!-- Banner: footwear -->
<section class="banner">
  <svg class="banner-shapes" viewBox="0 0 270 620" aria-hidden="true">
    <rect width="270" height="620" fill="var(--white)"/>
    <polygon points="0,0 270,0 270,100 0,66" fill="var(--grey-light)"/>
    <polygon points="0,62 270,96 270,106 0,72" fill="var(--black)"/>
    <polygon points="0,282 270,330 270,340 0,292" fill="var(--black)"/>
    <polygon points="0,292 160,320 0,360" fill="var(--grey-mid)"/>
    <polygon points="0,540 125,598 0,598" fill="var(--red)"/>
    <polygon points="150,598 270,560 270,620 150,620" fill="var(--grey-light)"/>
  </svg>
  <div class="photo photo--runway" role="img" aria-label="Embellished floral heels walking on a runway"></div>
  <div class="brand">Harlow and Vine<br>Training Center</div>
  <h2 class="headline" style="top:342px">FOOTWEAR<br>DESIGN AND PRODUCT<br>DEVELOPMENT<span class="rule"></span></h2>
  <div class="details" style="top:428px">
    <h3>KPL Diploma in Fashion Technology</h3>
    <p>+ 3 months Full-Time or 1 year Part-Time Programme<br>+ 13 industry-focused KPL modules</p>
    <h3>Funding &amp; Career Opportunities</h3>
    <p>Speak to us today about your eligibility in funding and potential career opportunities.</p>
  </div>
  <ul class="contacts">
    <li><svg viewBox="0 0 10 10"><path d="M2 1l2 2-1 1.5a6 6 0 0 0 2.5 2.5L7 6l2 2-1.5 1.5C4 9 1 6 .5 2.5z" fill="#fff"/></svg>64208830</li>
    <li><svg viewBox="0 0 10 10"><rect x="0.5" y="2" width="9" height="6" fill="none" stroke="#fff"/><path d="M.5 2l4.5 3.5L9.5 2" fill="none" stroke="#fff"/></svg>enquiry@havtc.org</li>
    <li><svg viewBox="0 0 10 10"><circle cx="5" cy="5" r="4.2" fill="none" stroke="#fff"/><path d="M1 5h8M5 1v8" stroke="#fff"/></svg>www.havtc.edu.sg</li>
  </ul>
  <div class="partners">
    <span class="partner"><span class="partner-square"></span>NB PLX Centre</span>
    <span class="partner"><span class="partner-circle"></span>Vero Mark</span>
  </div>
</section>

</body>
</html>
```